Brookfarrow Osteopathy and dry needling business card

Business card for Brookfarrow Osteopathy and Dry Needling.

Industry/Entity Type

Health

Contact Information for Business Card

I do not have a phone number yet. I also do not have an email address yet. The physical address is: 48 Lower Crane Street Brookfarrow The website is: www.brookfarrowosteosteopathy.example My details are: Dr Martin Pellowe, Osteopath (B.Clin.Sci (Ost) M.Ost BSC ECON (Hons)

Colors
0094D4
00A9DD
6FCCEA
C7EBF8
E9F6FB

Requirements
Must have
• logo on the back
Nice to have
• Maybe a space for me to write an appointment time and date on the card.

```html
<!DOCTYPE html>
<html lang="en">
<head>
<meta charset="utf-8">
<title>Brookfarrow Osteopathy and Dry Needling – Business Card</title>
<link rel="stylesheet" href="https://fonts.googleapis.com/css2?family=Arimo:wght@400;700&display=swap">
<style>
  :root {
    --backdrop: #1c1c1c;
    --card-white: #f3f3f3;
    --brand-blue: #0f90ca;
    --accent-orange: #f08b2d;
    --text-white: #ffffff;
  }
  * { margin: 0; padding: 0; box-sizing: border-box; }
  html, body {
    width: 1200px; height: 1059px; overflow: hidden;
    background: var(--backdrop);
    font-family: "Arimo", Arial, sans-serif;
  }
  .stage { position: relative; width: 1200px; height: 1059px; }
  .card {
    position: absolute; width: 690px; height: 392px;
    border-radius: 22px; overflow: hidden;
    box-shadow: 0 10px 28px rgba(0,0,0,0.55);
  }
  .card-front { left: 256px; top: 89px; background: var(--card-white); }
  .card-back { left: 255px; top: 547px; background: var(--brand-blue); }
  .front-art { position: absolute; inset: 0; }
  .brand-mark {
    position: absolute; left: 470px; top: 52px; width: 190px;
    display: flex; align-items: center; gap: 10px;
  }
  .brand-dot {
    flex: none; width: 26px; height: 26px; border-radius: 50%;
    border: 2px solid var(--brand-blue);
  }
  .brand-name {
    color: var(--brand-blue); font-weight: 700; font-size: 15px;
    line-height: 1.25; text-transform: uppercase; letter-spacing: 0.5px;
  }
  .practitioner { position: absolute; left: 34px; top: 268px; }
  .practitioner-name {
    color: var(--accent-orange); font-weight: 700; font-size: 24.5px;
    text-transform: uppercase; letter-spacing: 0.2px;
  }
  .practitioner-title {
    color: var(--text-white); font-size: 17.5px; margin-top: 6px;
  }
  .contact-row {
    position: absolute; left: 34px; right: 34px; top: 344px;
    display: flex; gap: 30px; color: var(--text-white);
    font-size: 15.5px; white-space: nowrap;
  }
  .contact-item { display: flex; align-items: center; gap: 8px; }
  .contact-item svg { flex: none; }
  .back-mark {
    position: absolute; left: 228px; top: 78px; width: 236px; height: 236px;
    border-radius: 50%; border: 2px solid var(--text-white);
    display: flex; align-items: center; justify-content: center; text-align: center;
  }
  .back-name {
    color: var(--text-white); font-weight: 700; font-size: 22px;
    line-height: 1.3; text-transform: uppercase; letter-spacing: 1px; padding: 0 20px;
  }
</style>
</head>
<body>
<main class="stage">
  <section class="card card-front" aria-label="Business card front">
    <svg class="front-art" viewBox="0 0 690 392" width="690" height="392">
      <path class="blue-field" fill="var(--brand-blue)"
        d="M0 250 C90 240 150 200 230 182 C310 165 380 190 450 222 C520 250 600 225 690 190 L690 392 L0 392 Z"/>
      <path role="img" aria-label="Stylised orange spine running across the card"
        fill="var(--accent-orange)" stroke="var(--card-white)" stroke-width="2"
        d="M0 242 C60 238 90 220 150 170 C200 140 240 132 300 138 C370 146 420 172 480 190 C540 205 600 180 650 160 L690 148 L690 185 C630 215 600 225 560 240 C520 252 480 250 440 238 C390 220 340 190 290 190 C240 190 190 210 150 230 C110 248 60 258 0 254 Z"/>
    </svg>
    <div class="brand-mark">
      <span class="brand-dot"></span>
      <span class="brand-name">Brookfarrow Osteopathy and Dry Needling</span>
    </div>
    <div class="practitioner">
      <h1 class="practitioner-name">Dr Martin Pellowe</h1>
      <p class="practitioner-title">Osteopath (B.Clin.Sci (Ost) M.Ost BSC ECON (Hons)</p>
    </div>
    <div class="contact-row">
      <span class="contact-item">
        <svg width="14" height="14" viewBox="0 0 14 14" fill="none" stroke="var(--accent-orange)" stroke-width="1.3">
          <circle cx="7" cy="7" r="6"/><ellipse cx="7" cy="7" rx="2.6" ry="6"/>
          <line x1="1" y1="7" x2="13" y2="7"/><line x1="2" y1="4" x2="12" y2="4"/><line x1="2" y1="10" x2="12" y2="10"/>
        </svg>
        www.brookfarrowosteosteopathy.example
      </span>
      <span class="contact-item">
        <svg width="12" height="16" viewBox="0 0 12 16">
          <path fill="var(--accent-orange)" d="M6 0C2.7 0 0 2.6 0 5.9 0 10 6 16 6 16s6-6 6-10.1C12 2.6 9.3 0 6 0zm0 8.3a2.4 2.4 0 1 1 0-4.8 2.4 2.4 0 0 1 0 4.8z"/>
        </svg>
        48 Lower Crane Street Brookfarrow
      </span>
    </div>
  </section>

  <section class="card card-back" aria-label="Business card back">
    <div class="back-mark">
      <span class="back-name">Brookfarrow Osteopathy and Dry Needling</span>
    </div>
  </section>
</main>
</body>
</html>
```